Banner Ad Design

Design 2 ad banners with animation: 468x60 and 160x160

The 2 ad banners should complement the look, feel and messaging of our new VANTA6 microphone campaign. Any of the product imagery from the homepage can be used as well. For Reference:

1) website: www.brindlewave-acoustics.com

2) print advertising: http://www.brindlewave-acoustics.com/Advertising/UNlike_the_Others_4.5.html

3) email: http://www.brindlewave-acoustics.com/ecampaign/UNlike/v6_sfdb.html

4) Product photo (if needed):
http://www.brindlewave-acoustics.com/images/Hi_Rz/MV-3KT_BL_headset_microphone.jpg

The small banner sizes will present an interesting challege so we can modify the copy as necessary but for the time being, we have:

NEW! VANTA6 Microphones
Tiny Enough. TOUGH Enough.
Delivers a knockout against the others.
GET a KNOCKOUT.

Target Market(s)

Audio production engineers (front of house guys) who manage the audio during live shows. Here is the online magazine for this target market; the 468x60 banner will rotate at the top of this website: http://www.stagerigdaily.com/

Requirements
Must have
• - Brindlewave Acoustics logo: http://www.brindlewave-acoustics.com/images/BWA_logo-R.jpg
• - Call to Action: GET A KNOCKOUT. ref: http://www.brindlewave-acoustics.com/ecampaign/UNlike/v6_sfdb.html

```html
<!DOCTYPE html>
<html lang="en">
<head>
<meta charset="utf-8">
<title>Brindlewave Acoustics — VANTA6 Banner Frames</title>
<link rel="stylesheet" href="https://fonts.googleapis.com/css2?family=Arimo:ital,wght@0,400;0,700;1,700&display=swap">
<style>
  :root {
    --page: #ffffff;
    --ink: #111111;
    --frame-line: #3a3a3a;
    --orange: #f7a233;
    --orange-deep: #e8891a;
    --panel-dark: #151515;
    --panel-mid: #3b3b3b;
    --grey-light: #f2f2f2;
    --grey-mid: #9a9a9a;
    --grey-dark: #5a5a5a;
    --logo-grey: #6b6b6b;
    --white: #ffffff;
  }
  * { box-sizing: border-box; margin: 0; padding: 0; }
  html, body {
    width: 1200px; height: 1200px; overflow: hidden;
    background: var(--page);
    font-family: "Arimo", Arial, sans-serif;
    color: var(--ink);
  }
  .sheet {
    position: relative;
    width: 850px; height: 850px;
    transform: scale(1.41176);
    transform-origin: 0 0;
  }
  .size-title {
    position: absolute; font-size: 16px; font-weight: 400;
    transform: translateX(-50%);
  }
  .frame-label {
    position: absolute; font-size: 16px; font-weight: 400;
    transform: translate(-50%, -50%);
    white-space: nowrap;
  }

  /* ---------- Leaderboard 468x60 ---------- */
  .leader {
    position: absolute; left: 226px; width: 467px; height: 60px;
    border: 1px solid var(--frame-line);
    overflow: hidden;
    background: linear-gradient(90deg, var(--grey-dark) 0%, var(--grey-mid) 18%, var(--grey-light) 45%, var(--grey-mid) 75%, var(--grey-dark) 100%);
  }
  .leader .brand {
    position: absolute; left: 0; top: 0; width: 75px; height: 100%;
    background: var(--white);
    display: flex; align-items: center; justify-content: center;
  }
  .leader .product {
    position: absolute; left: 76px; top: 6px; width: 100px; height: 47px;
    border-radius: 3px 0 0 3px;
    background: linear-gradient(180deg, var(--panel-mid) 0%, var(--panel-dark) 55%);
    color: var(--white); font-weight: 700; font-size: 11.5px; line-height: 13px;
    display: flex; flex-direction: column; justify-content: center; padding-left: 9px;
  }
  .leader .message {
    position: absolute; left: 176px; top: 6px; width: 175px; height: 47px;
    background: linear-gradient(180deg, var(--orange) 0%, var(--orange-deep) 100%);
    color: var(--white); font-weight: 700;
    display: flex; flex-direction: column; justify-content: center; align-items: center;
    text-align: center;
  }
  .leader .message.caps { font-size: 13px; line-height: 14px; }
  .leader .message.italic { font-style: italic; font-size: 14px; line-height: 16px; color: var(--ink); }
  .leader .message.cta { font-size: 18px; }
  .leader .visual { position: absolute; left: 342px; top: 0; width: 125px; height: 60px; }

  /* ---------- Square 160x160 ---------- */
  .square {
    position: absolute; left: 378px; width: 161px; height: 161px;
    border: 1px solid var(--frame-line);
    overflow: hidden;
    background: linear-gradient(90deg, var(--grey-mid) 0%, var(--grey-light) 45%, var(--grey-mid) 100%);
  }
  .square .brand {
    position: absolute; left: 0; top: 0; width: 100%; height: 40px;
    background: linear-gradient(180deg, var(--white) 70%, rgba(255,255,255,0) 100%);
    display: flex; align-items: center; justify-content: center;
  }
  .square .visual { position: absolute; left: 90px; top: 55px; width: 70px; height: 105px; }
  .square .product {
    position: absolute; left: 13px; top: 38px; width: 133px; height: 44px;
    border-radius: 5px 5px 0 0;
    background: linear-gradient(180deg, var(--panel-mid) 0%, var(--panel-dark) 50%);
    color: var(--white); font-weight: 700; font-size: 11.5px; line-height: 13px;
    display: flex; flex-direction: column; justify-content: center; align-items: center;
  }
  .square .message {
    position: absolute; left: 13px; top: 88px; width: 108px; height: 64px;
    border-radius: 0 0 0 5px;
    background: linear-gradient(180deg, var(--orange) 0%, var(--orange-deep) 100%);
    color: var(--white); font-weight: 700;
    display: flex; flex-direction: column; justify-content: center;
  }
  .square .message.caps { font-size: 11.5px; line-height: 12px; padding-left: 10px; }
  .square .message.italic { font-style: italic; font-size: 11.5px; line-height: 13.5px; color: var(--ink); padding-left: 5px; }
  .square .message.cta { padding-left: 15px; }
  .square .message.cta .big { font-size: 16px; line-height: 18px; }
  .square .message.cta .small { font-size: 12px; line-height: 14px; padding-left: 6px; }

  .brand-name {
    display: flex; align-items: center; gap: 3px;
    color: var(--logo-grey); font-weight: 700; font-size: 11px; letter-spacing: 0.2px;
  }
  .brand-dot { width: 7px; height: 7px; border-radius: 50%; background: var(--orange); }
  .square .brand-name { font-size: 13px; }
  .square .brand-dot { width: 8px; height: 8px; }
</style>
</head>
<body>
<main class="sheet">

  <h2 class="size-title" style="left:468px; top:20px;">468X60</h2>

  <span class="frame-label" style="left:165px; top:73px;">Frame A</span>
  <section class="leader" style="top:43px;">
    <div class="brand"><span class="brand-name"><span class="brand-dot"></span>Brindlewave</span></div>
    <div class="product"><span>NEW VANTA6</span><span>MICROPHONE</span></div>
    <div class="message caps"><span>TINY ENOUGH</span><span>THOUGH ENOUGH</span></div>
    <svg class="visual" viewBox="0 0 125 60" role="img" aria-label="Side profile of a performer wearing the headset microphone">
      <defs><linearGradient id="pa" x1="0" x2="1"><stop offset="0" stop-color="#b8b8b8"/><stop offset="1" stop-color="#4a4a4a"/></linearGradient></defs>
      <path d="M16 60 Q20 20 45 0 L125 0 L125 60 Z" fill="url(#pa)"/>
      <path d="M4 60 Q10 18 40 0 L46 0 Q18 20 12 60 Z" fill="var(--orange)"/>
      <rect x="106" y="8" width="12" height="44" rx="6" fill="var(--orange)"/>
    </svg>
  </section>

  <span class="frame-label" style="left:165px; top:142px;">Frame B</span>
  <section class="leader" style="top:112px;">
    <div class="brand"><span class="brand-name"><span class="brand-dot"></span>Brindlewave</span></div>
    <div class="product"><span>NEW VANTA6</span><span>MICROPHONE</span></div>
    <div class="message italic"><span>Delivers A Knockout</span><span>Against The Others</span></div>
    <svg class="visual" viewBox="0 0 125 60" role="img" aria-label="Side profile of a performer wearing the headset microphone">
      <path d="M16 60 Q20 20 45 0 L125 0 L125 60 Z" fill="url(#pa)"/>
      <path d="M4 60 Q10 18 40 0 L46 0 Q18 20 12 60 Z" fill="var(--orange)"/>
      <rect x="106" y="8" width="12" height="44" rx="6" fill="var(--orange)"/>
    </svg>
  </section>

  <span class="frame-label" style="left:165px; top:210px;">Frame C</span>
  <section class="leader" style="top:181px;">
    <div class="brand"><span class="brand-name"><span class="brand-dot"></span>Brindlewave</span></div>
    <div class="product"><span>NEW VANTA6</span><span>MICROPHONE</span></div>
    <div class="message cta"><span>Get A Knockout</span></div>
    <svg class="visual" viewBox="0 0 125 60" role="img" aria-label="Side profile of a performer wearing the headset microphone">
      <path d="M16 60 Q20 20 45 0 L125 0 L125 60 Z" fill="url(#pa)"/>
      <path d="M4 60 Q10 18 40 0 L46 0 Q18 20 12 60 Z" fill="var(--orange)"/>
      <rect x="106" y="8" width="12" height="44" rx="6" fill="var(--orange)"/>
    </svg>
  </section>

  <h2 class="size-title" style="left:452px; top:292px;">160X160</h2>

  <span class="frame-label" style="left:320px; top:400px;">Frame A</span>
  <section class="square" style="top:320px;">
    <svg class="visual" viewBox="0 0 70 105" role="img" aria-label="Side profile of a performer wearing the headset microphone">
      <path d="M18 105 Q22 40 70 18 L70 105 Z" fill="url(#pa)"/>
      <path d="M8 105 Q14 30 70 8 L70 14 Q20 36 15 105 Z" fill="var(--orange)"/>
    </svg>
    <div class="brand"><span class="brand-name"><span class="brand-dot"></span>Brindlewave</span></div>
    <div class="product"><span>NEW VANTA6</span><span>MICROPHONE</span></div>
    <div class="message caps"><span>TINY</span><span>ENOUGH</span><span>THOUGH</span><span>ENOUGH</span></div>
  </section>

  <span class="frame-label" style="left:320px; top:567px;">Frame B</span>
  <section class="square" style="top:489px;">
    <svg class="visual" viewBox="0 0 70 105" role="img" aria-label="Side profile of a performer wearing the headset microphone">
      <path d="M18 105 Q22 40 70 18 L70 105 Z" fill="url(#pa)"/>
      <path d="M8 105 Q14 30 70 8 L70 14 Q20 36 15 105 Z" fill="var(--orange)"/>
    </svg>
    <div class="brand"><span class="brand-name"><span class="brand-dot"></span>Brindlewave</span></div>
    <div class="product"><span>NEW VANTA6</span><span>MICROPHONE</span></div>
    <div class="message italic"><span>Delivers A</span><span>Knockout</span><span>Against The</span><span>Others</span></div>
  </section>

  <span class="frame-label" style="left:320px; top:736px;">Frame C</span>
  <section class="square" style="top:659px;">
    <svg class="visual" viewBox="0 0 70 105" role="img" aria-label="Side profile of a performer wearing the headset microphone">
      <path d="M18 105 Q22 40 70 18 L70 105 Z" fill="url(#pa)"/>
      <path d="M8 105 Q14 30 70 8 L70 14 Q20 36 15 105 Z" fill="var(--orange)"/>
    </svg>
    <div class="brand"><span class="brand-name"><span class="brand-dot"></span>Brindlewave</span></div>
    <div class="product"><span>NEW VANTA6</span><span>MICROPHONE</span></div>
    <div class="message cta"><span class="big">Get A</span><span class="small">Knockout</span></div>
  </section>

</main>
</body>
</html>
```